PLEASE READ - DESIGN for Music Cover Tunevault - DJ and Female Singer

A nice cover to be put on Tunevault.
Definitely will be on Tunevault and All Media
Name of the song: Marivella
Singer name: Tara Wolskind
DJ name: DJ Roland Kestry

Marivella definition: A desire to be in the Sun

We need eye catching icon or something that can attract people's eyes when they see it immediately. Design must be elegant. This is not some type of Club Banging Music. The singer is a romantic and sophisticated audiophile jazz acoustic recording artist. DJ is not playing in some clubs but exclusive.

Photo of singer and DJ can be on the cover OR just photo of the singer OR just an Icon wifh their names and the song name.

Avoid these colors: Pink, Purple, Silver !!
For the background color try: A mixed of Black or Gold with Elegant Yellow, Pastel Orange, or light Blue.
For name of the song and Icon color : can be of Gold or even Red or White.
Or you can try and mix it all up yourself

Icon ideas: can be a combination of letter Capital C with small B & Capital V alone or mixed with a sun logo or half of Sun. Some cool stuff.
CB is Tara Wolskind
V is for the DJ name

Target Market(s)

Young Adult, Lounge Crowd, Club Goers / Lounge Goers, Ladies, Executives, Adults, Music Industry

Industry/Entity Type

Entertainment Industry

Font styles to use
Serif

Requirements
Must have
• MARIVELLA ( song name )
• Available on Tunevault logo
• EYE CATCHING ICON or LOGO
Should not have
• Avoid this color :
• Pink, Purple, Silver, White
• Our first project was already consisting these colors, we will attach the old design of the first song but PLEASE DO NOT apply the older design to this new project :)

```html
<!DOCTYPE html>
<html lang="en">
<head>
<meta charset="utf-8">
<title>Marivella — Tara Wolskind and DJ Roland Kestry</title>
<link rel="stylesheet" href="https://fonts.googleapis.com/css2?family=Cinzel:wght@600;700&display=swap">
<style>
  :root {
    --gold: #e6b740;
    --gold-deep: #a8780f;
    --amber: #e9a65a;
    --peach: #f3c9a2;
    --sky: #b9d9e4;
    --umber: #4a2e18;
    --ink: #0b0b0b;
  }
  html, body {
    margin: 0;
    padding: 0;
    width: 1200px;
    height: 1200px;
    overflow: hidden;
    background: var(--ink);
  }
  .cover {
    position: relative;
    width: 1200px;
    height: 1200px;
    overflow: hidden;
    font-family: "Cinzel", serif;
  }
  .cover-art {
    position: absolute;
    inset: 0;
    background:
      radial-gradient(ellipse 260px 240px at 250px 640px, rgba(255,248,215,0.95), rgba(255,240,200,0) 70%),
      radial-gradient(ellipse 380px 520px at 1000px 420px, rgba(190,160,130,0.85), rgba(190,160,130,0) 70%),
      radial-gradient(ellipse 300px 260px at 820px 180px, rgba(185,217,228,0.7), rgba(185,217,228,0) 70%),
      linear-gradient(160deg, #f7dc7a 0%, #f2c04e 22%, #c98a3a 40%, #e9c18e 60%, #c98a55 80%, #9a6438 100%);
  }
  .cover-shade {
    position: absolute;
    left: 0;
    right: 0;
    bottom: 0;
    height: 420px;
    background: linear-gradient(180deg, rgba(11,11,11,0) 0%, rgba(30,18,8,0.7) 45%, rgba(11,11,11,0.92) 100%);
  }
  .store-badge {
    position: absolute;
    left: 36px;
    top: 34px;
    width: 246px;
    height: 80px;
    background: var(--ink);
    display: flex;
    align-items: center;
    gap: 12px;
    padding: 0 16px;
    box-sizing: border-box;
    color: var(--gold);
  }
  .store-badge .mark {
    width: 26px;
    height: 26px;
    border-radius: 50%;
    background: var(--gold);
    flex: none;
  }
  .store-badge .label { line-height: 1; }
  .store-badge .label small {
    display: block;
    font-size: 14px;
    font-weight: 600;
    margin-bottom: 6px;
  }
  .store-badge .label strong {
    display: block;
    font-size: 26px;
    font-weight: 700;
  }
  .duo-mark {
    position: absolute;
    left: 42px;
    top: 912px;
    width: 192px;
    height: 192px;
    border-radius: 50%;
    background: var(--gold);
    display: flex;
    align-items: center;
    justify-content: center;
    color: var(--ink);
    font-size: 34px;
    font-weight: 700;
    letter-spacing: 2px;
  }
  .titles {
    position: absolute;
    left: 0;
    top: 0;
    width: 1200px;
    height: 1200px;
  }
  .song-title {
    fill: var(--gold);
    font-family: "Cinzel", serif;
    font-weight: 700;
    font-size: 112px;
  }
  .artist-credit {
    fill: var(--gold);
    font-family: "Cinzel", serif;
    font-weight: 600;
    font-size: 24px;
  }
</style>
</head>
<body>
  <main class="cover">
    <div class="cover-art" role="img" aria-label="Portrait of the singer behind sweeping golden light streaks and a glowing sun"></div>
    <div class="cover-shade"></div>

    <div class="store-badge">
      <span class="mark"></span>
      <span class="label"><small>Available on</small><strong>Tunevault</strong></span>
    </div>

    <div class="duo-mark">TWRK</div>

    <svg class="titles" viewBox="0 0 1200 1200" width="1200" height="1200">
      <text class="song-title" x="276" y="1048" textLength="798" lengthAdjust="spacingAndGlyphs">MARIVELLA</text>
      <text class="artist-credit" x="312" y="1114" textLength="730" lengthAdjust="spacing">TARA WOLSKIND AND DJ ROLAND KESTRY</text>
    </svg>
  </main>
</body>
</html>
```